A tri fold flyer to be sent to parents advertising Learning Center, tutoring in math or language after school and on weekendsSince 1994 the Bright Owl Study House has been helping the children on Oahu do better in school. Bright Owl has developed a successful method of teaching math, reading and writing for students in grades K-12. Affordable and effective, it's unlike any other learning system.

Target Market(s)

Parents of school age kids

Industry/Entity Type

Education

Font styles to use
Sans Serif

Requirements
Must have
• same text as in previews
Nice to have
• 3 fold
Should not have
• mistakes

```html
<!DOCTYPE html>
<html lang="en">
<head>
<meta charset="utf-8">
<title>Bright Owl Study House – Tri-fold Flyer</title>
<link href="https://fonts.googleapis.com/css2?family=Raleway:wght@400;500;600;700&display=swap" rel="stylesheet">
<style>
:root{
  --teal:#5fbcbc;
  --teal-deep:#1fa3b0;
  --teal-dark:#1e96a6;
  --teal-pale:#e3f3f3;
  --green:#9cc83a;
  --orange:#f8ab3d;
  --blue:#2aa6de;
  --yellow:#f6d200;
  --ink:#5a5a5a;
  --white:#ffffff;
  --stage:#d7d8da;
}
*{box-sizing:border-box;margin:0;padding:0}
html,body{width:1200px;height:672px;overflow:hidden;background:var(--stage);font-family:"Raleway",sans-serif}
.canvas{position:relative;width:1200px;height:672px}
.spread{position:absolute;left:70px;top:56px;width:745px;height:578px;display:flex}
.panel{position:relative;width:248px;height:578px;overflow:hidden;color:var(--white)}
.panel--mid{width:249px}
.waves{position:absolute;left:0;top:0;width:100%;height:100%}
.photo{position:absolute}
.body-copy{position:absolute;font-size:10px;line-height:1.36;text-align:justify}
.body-copy p{margin-bottom:10px}
.body-copy p:last-child{margin-bottom:0}
.circle{position:absolute;border-radius:50%;display:flex;align-items:center;justify-content:center;text-align:center;color:var(--white);font-size:8.5px;line-height:1.15;font-weight:500}
.circle--blue{background:var(--blue)}
.circle--orange{background:var(--orange)}
.circle--yellow{background:var(--yellow)}
.panel-title{position:absolute;left:14px;top:40px;font-size:19px;font-weight:400;color:var(--teal-deep);letter-spacing:.3px}
.panel-subtitle{position:absolute;left:14px;top:67px;font-size:12.5px;line-height:1.2;color:var(--teal-deep);font-weight:500}
.web{position:absolute;left:0;width:100%;text-align:center;font-size:13px;color:var(--ink);letter-spacing:.2px}
.section-head{position:absolute;font-size:11.5px;line-height:1.4;font-weight:400}
.section-head strong{font-weight:400;font-size:12.5px}
.cover{position:absolute;left:887px;top:58px;width:257px;height:568px;overflow:hidden;background:var(--white)}
.brand{position:absolute;left:0;top:412px;width:100%;text-align:center;color:var(--white);font-weight:600;letter-spacing:4px;line-height:1.05}
.brand__main{font-size:30px;letter-spacing:2px}
.brand__sub{font-size:18px}
.cover-tagline{position:absolute;left:0;top:500px;width:100%;text-align:center;color:var(--white);font-size:12px;line-height:1.4}
.cover-footer{position:absolute;left:0;top:540px;width:100%;height:28px;background:var(--white);display:flex;align-items:center;justify-content:center;color:var(--ink);font-size:13px}
</style>
</head>
<body>
<div class="canvas">

  <div class="spread">

    <section class="panel">
      <svg class="waves" viewBox="0 0 248 578" preserveAspectRatio="none" aria-hidden="true">
        <rect width="248" height="578" fill="#5fbcbc"/>
        <path d="M0 0H248V150C190 190 120 120 0 170Z" fill="#e3f3f3"/>
        <path d="M0 340C80 310 170 330 248 300V360H0Z" fill="#9cc83a"/>
        <path d="M0 348C80 322 170 345 248 318V360H0Z" fill="#ffffff" opacity=".85"/>
        <rect y="505" width="248" height="73" fill="#ffffff"/>
      </svg>
      <div class="photo" style="left:0;top:352px;width:248px;height:160px;background:linear-gradient(160deg,#7f8fa6,#2d4f9a 55%,#3a3a55)" role="img" aria-label="Group photo of smiling students in blue shirts"></div>
      <svg class="waves" viewBox="0 0 248 578" preserveAspectRatio="none" aria-hidden="true">
        <path d="M0 338C70 330 150 350 248 340V352H0Z" fill="#5fbcbc"/>
        <path d="M0 505C90 470 180 520 248 490V578H0Z" fill="#9cc83a"/>
        <path d="M0 512C90 482 180 530 248 500V578H0Z" fill="#ffffff"/>
      </svg>
      <h2 class="panel-title">WHAT WE DO</h2>
      <p class="panel-subtitle">Personalized<br>instruction makes<br>learning fun!</p>
      <div class="circle circle--blue" style="left:164px;top:9px;width:50px;height:50px">language<br>arts</div>
      <div class="circle circle--orange" style="left:164px;top:60px;width:50px;height:50px;font-size:10px">math</div>
      <div class="circle circle--yellow" style="left:164px;top:111px;width:50px;height:50px">SSAT<br>preparation</div>
      <div class="body-copy" style="left:14px;top:177px;width:222px">
        <p>Since 1994 the Bright Owl Study House has been helping the children on Oahu do better in school.</p>
        <p>Bright Owl has developed a successful method of teaching math, reading and writing for students in grades K-12.</p>
        <p>Affordable and effective, it's unlike any other learning system.</p>
      </div>
      <p class="web" style="top:548px">www.brightowlhawaii.com</p>
    </section>

    <section class="panel panel--mid">
      <svg class="waves" viewBox="0 0 249 578" preserveAspectRatio="none" aria-hidden="true">
        <rect width="249" height="578" fill="#5fbcbc"/>
        <rect y="500" width="249" height="78" fill="#1fa3b0"/>
      </svg>
      <div class="photo" style="left:0;top:20px;width:249px;height:180px;background:linear-gradient(120deg,#6f8f7a,#c9b59a 50%,#d9d3c6)" role="img" aria-label="Girl and tutor giving a high five at a classroom desk"></div>
      <svg class="waves" viewBox="0 0 249 578" preserveAspectRatio="none" aria-hidden="true">
        <path d="M0 0H249V10C180 5 110 45 0 30Z" fill="#e3f3f3"/>
        <path d="M0 30C60 20 90 50 60 60C30 70 10 50 0 55Z" fill="#1fa3b0"/>
        <path d="M0 185C90 215 160 160 249 178V215H0Z" fill="#9cc83a"/>
        <path d="M0 195C90 222 170 172 249 190V230H0Z" fill="#e3f3f3"/>
        <path d="M0 208C90 235 170 188 249 205V240H0Z" fill="#5fbcbc"/>
      </svg>
      <div class="section-head" style="left:13px;top:244px"><span>MORE THAN JUST TUTORING…</span><br><strong>It's a better way of learning</strong></div>
      <div class="body-copy" style="left:13px;top:288px;width:224px">
        <p>Rather than simply walking students through worksheets or being a homework assistant, Bright Owl is a productive and exciting way to learn.</p>
        <p>Lessons are designed to accommodate students at any ability level. All students (remedial, average and gifted) benefit because the programs are personalized.</p>
        <p>Pre and post tests measure the student's progress. Outstanding improvement is made because every lesson is designed to challenge the student while ensuring that a specific skill is mastered.</p>
      </div>
      <div class="body-copy" style="left:13px;top:512px;width:224px">
        <p>Lessons are an extended hour long (70 minutes), most kids come twice a week; the charge is $35 per lesson.</p>
      </div>
    </section>

    <section class="panel">
      <svg class="waves" viewBox="0 0 248 578" preserveAspectRatio="none" aria-hidden="true">
        <rect width="248" height="578" fill="#f8ab3d"/>
      </svg>
      <div class="photo" style="left:0;top:280px;width:248px;height:170px;background:linear-gradient(100deg,#7a3a30,#c89a7c 45%,#ece3d4)" role="img" aria-label="Student writing at a desk in a study room"></div>
      <svg class="waves" viewBox="0 0 248 578" preserveAspectRatio="none" aria-hidden="true">
        <path d="M0 262C90 240 170 290 248 265V300C170 320 90 270 0 292Z" fill="#1fa3b0"/>
        <path d="M0 283C90 262 170 310 248 288V300C170 322 90 275 0 297Z" fill="#e3f3f3"/>
        <path d="M0 440C90 460 170 420 248 430V460H0Z" fill="#5fbcbc"/>
        <path d="M0 450C90 470 170 432 248 442V578H0Z" fill="#f8ab3d"/>
      </svg>
      <div class="section-head" style="left:13px;top:24px"><strong>It really is a better way of learning…</strong></div>
      <div class="body-copy" style="left:13px;top:63px;width:224px">
        <p>Each lesson has a variety of learning activities, which include personalized instruction, hands on manipulatives and individual computer sessions.</p>
        <p>This multisensory method of instruction provides the maximum amount of learning in the minimum amount of time.</p>
        <p>Bright Owl students have experiences of being successful, which builds their confidence.</p>
      </div>
      <div class="section-head" style="left:13px;top:466px"><strong>Two lessons a week can make a big difference.</strong></div>
      <div class="body-copy" style="left:13px;top:504px;width:224px">
        <p>We offer lessons Monday – Saturday year round. This is our basic schedule. On school days, the first lesson is at 2:30. When you register we look at both our schedule and yours to see what works for both of us.</p>
      </div>
    </section>
  </div>

  <section class="cover">
    <div class="photo" style="left:20px;top:20px;width:225px;height:360px;background:linear-gradient(180deg,#ffffff,#e9ecef 40%,#9aa3ad 70%,#3f4f6a)" role="img" aria-label="Smiling boy holding up a small whiteboard sign"></div>
    <svg class="waves" viewBox="0 0 257 568" preserveAspectRatio="none" aria-hidden="true">
      <path d="M0 390C90 350 170 400 257 370V390C170 418 90 372 0 405Z" fill="#9cc83a"/>
      <path d="M0 400C90 365 170 412 257 385V568H0Z" fill="#5fbcbc"/>
    </svg>
    <div class="circle circle--blue" style="left:190px;top:251px;width:56px;height:56px;font-size:9px">language<br>arts</div>
    <div class="circle circle--orange" style="left:190px;top:307px;width:56px;height:56px;font-size:11px">math</div>
    <div class="circle circle--yellow" style="left:190px;top:363px;width:56px;height:56px;font-size:9px">SSAT<br>preparation</div>
    <div class="brand"><div class="brand__main">BRIGHT OWL</div><div class="brand__sub">HAWAII</div></div>
    <p class="cover-tagline">MORE THAN JUST TUTORING…<br>It's a better way of learning</p>
    <div class="cover-footer">www.brightowlhawaii.com</div>
  </section>

</div>
</body>
</html>
```